Ridgeline Orchards Organic Cherry POS card 7x11

We are wanting to create a one-sided 7 x 11 organic cherry card that is eye catching and informative.This should be clear and easy to read and not cluttered. We use these cards as a display in grocery stores, demo stands, and other events to market Organic Ridgeline Sweet Orchards. We have a few facts that we would like displayed on the card (see attachment).

Target Market(s)

Consumers

Industry/Entity Type

Agriculture

Requirements
Must have
• Natural color palettes
• Easy to read
• Ridgeline Orchards
Nice to have
• Unique, realistic cherry design

```html
<!DOCTYPE html>
<html lang="en">
<head>
<meta charset="utf-8">
<title>Ridgeline Orchards – Organic Cherry Card</title>
<link href="https://fonts.googleapis.com/css2?family=Oswald:wght@700&family=Lilita+One&family=Courgette&display=swap" rel="stylesheet">
<style>
  :root {
    --olive: #a9ae7f;
    --banner: #8cc63f;
    --banner-dark: #6fa32c;
    --ink: #2a1a12;
    --badge: #3a8d43;
    --badge-ring: #7dc242;
    --ribbon: #4aa455;
    --ribbon-light: #6cc070;
    --ribbon-fold: #2f7a3a;
    --cherry: #c8161d;
    --cherry-dark: #6e0a0e;
    --white: #ffffff;
  }
  * { margin: 0; padding: 0; box-sizing: border-box; }
  html, body { width: 1200px; height: 764px; overflow: hidden; background: var(--olive); }
  .card { position: relative; width: 1200px; height: 764px; background: var(--olive); overflow: hidden; }

  .headline-banner { position: absolute; left: 0; top: 0; width: 1200px; height: 200px; }
  .headline {
    position: absolute; left: 60px; top: 36px; width: 1080px;
    font-family: "Oswald", sans-serif; font-weight: 700; color: var(--ink);
    text-align: center; text-transform: uppercase; line-height: 54px;
    font-size: 45px; letter-spacing: 2px; white-space: nowrap;
  }
  .headline span { display: block; }

  .cherry-photo { position: absolute; }
  .cherry-left {
    left: -20px; top: 420px; width: 290px; height: 310px; border-radius: 48% 52% 45% 55%;
    background: radial-gradient(circle at 40% 30%, #e8464a 0%, var(--cherry) 40%, var(--cherry-dark) 100%);
  }
  .cherry-cluster {
    left: 850px; top: 488px; width: 380px; height: 300px; border-radius: 40% 20% 0 45%;
    background:
      radial-gradient(circle at 72% 40%, #e0383d 0%, var(--cherry) 25%, transparent 42%),
      radial-gradient(circle at 30% 65%, #d92a30 0%, var(--cherry) 28%, transparent 45%),
      radial-gradient(circle at 70% 85%, #d92a30 0%, var(--cherry) 25%, var(--cherry-dark) 60%);
  }

  .fact-ribbon { position: absolute; left: 0; top: 170px; width: 520px; height: 594px; }
  .ribbon-text { position: absolute; color: var(--white); text-align: center; white-space: nowrap; }
  .ribbon-brand {
    left: 80px; top: 276px; width: 350px; transform: rotate(-4deg);
    font-family: "Lilita One", sans-serif; font-size: 30px; line-height: 1.05; text-transform: uppercase;
  }
  .ribbon-fact {
    left: 40px; top: 396px; width: 440px; transform: rotate(-4deg);
    font-family: "Courgette", cursive; font-size: 50px;
  }
  .ribbon-fact-end {
    left: 115px; top: 532px; width: 320px; transform: rotate(-4deg);
    font-family: "Courgette", cursive; font-size: 28px;
  }

  .badge {
    position: absolute; border-radius: 50%; background: var(--badge);
    border: 6px solid var(--badge-ring);
    display: flex; align-items: center; justify-content: center; text-align: center;
    font-family: "Courgette", cursive; color: var(--white); line-height: 1.1;
  }
  .badge-fat { left: 458px; top: 192px; width: 224px; height: 224px; font-size: 58px; line-height: 0.95; }
  .badge-fat::after { content: ""; position: absolute; inset: 8px; border: 2px solid rgba(255,255,255,.8); border-radius: 50%; }
  .badge-potassium { left: 692px; top: 176px; width: 216px; height: 216px; font-size: 30px; }
  .badge-vitamin { left: 916px; top: 196px; width: 224px; height: 224px; font-size: 32px; }
  .badge-melatonin { left: 606px; top: 364px; width: 208px; height: 208px; font-size: 30px; }
  .badge-inflammatory { left: 812px; top: 396px; width: 224px; height: 224px; font-size: 28px; border-style: dotted; border-width: 8px; }

  .brand-mark {
    position: absolute; left: 440px; top: 634px; display: flex; align-items: center; gap: 14px;
    font-family: "Courgette", cursive; font-size: 40px; color: var(--ink); white-space: nowrap;
  }
  .brand-mark .dot { width: 44px; height: 44px; border-radius: 50%; background: var(--cherry-dark); }
</style>
</head>
<body>
<main class="card">
  <div class="cherry-photo cherry-left" role="img" aria-label="Photograph of a ripe red cherry"></div>
  <div class="cherry-photo cherry-cluster" role="img" aria-label="Photograph of a cluster of red cherries with stems"></div>

  <svg class="fact-ribbon" viewBox="0 170 520 594" aria-hidden="true">
    <polygon points="250,172 332,172 340,270 262,276" fill="var(--ribbon-fold)"/>
    <polygon points="76,272 428,246 436,350 84,376" fill="var(--ribbon-light)"/>
    <polygon points="84,376 250,364 240,390 32,400" fill="var(--ribbon-fold)"/>
    <polygon points="32,386 486,354 494,468 40,500" fill="var(--ribbon)"/>
    <polygon points="112,510 300,496 292,520 120,524" fill="var(--ribbon-fold)"/>
    <polygon points="112,514 432,492 440,588 120,610" fill="var(--ribbon-light)"/>
    <polygon points="186,606 262,600 270,764 186,764" fill="var(--ribbon)"/>
    <polygon points="186,606 262,600 232,640" fill="var(--ribbon-fold)"/>
  </svg>

  <svg class="headline-banner" viewBox="0 0 1200 200" aria-hidden="true">
    <polygon points="48,20 1152,20 1125,96 1152,172 48,172 75,96" fill="var(--banner)"/>
    <rect x="48" y="168" width="1104" height="6" fill="var(--banner-dark)" opacity=".6"/>
  </svg>
  <h1 class="headline"><span>Washington State is the nation's</span><span>largest producer of organic cherries</span></h1>

  <p class="ribbon-text ribbon-brand">Organic<br>Ridgeline Cherries</p>
  <p class="ribbon-text ribbon-fact">make up 1/3 of</p>
  <p class="ribbon-text ribbon-fact-end">the nation's production</p>

  <div class="badge badge-fat">Fat<br>Free</div>
  <div class="badge badge-potassium">Source of<br>Potassium</div>
  <div class="badge badge-vitamin">Source<br>of<br>Vitamin C</div>
  <div class="badge badge-melatonin">Source of<br>Melatonin</div>
  <div class="badge badge-inflammatory">A Natural<br>Anti-<br>Inflammatory</div>

  <div class="brand-mark"><span class="dot"></span><span>Ridgeline Orchards</span></div>
</main>
</body>
</html>
```